I require a set of preaching screens for our Easter weekend.

1. Good Friday Service Title: Still Lanterns
2. Easter Sunday Service Title Bright Harbor
3. Message Title Screen Title Bright Harbor
Overview
We need a set of clean, minimal screen graphics for 3 service sermon series called Bright Harbor
All screens must be delivered at 1920x1080px (16:9), suitable for projection in a church auditorium.

Design style
Minimal and clean. Uncluttered. Strong typography. Subtle use of imagery or texture — nothing busy or overly decorative.

The tone should feel thoughtful and weighty without being dark or heavy.

Subtitle: Letters Written Beside a Quiet Harbor Gate
Date range: 1 March – 5 April

Branding
No existing branding to match. Designer has creative freedom on colour palette and typography, provided the overall feel remains minimal and clean.
What to avoid
Busy backgrounds or heavy textures
All files in PNG at 1920x1080px
Editable source files (PSD or AI)

Please use images below as you feel is appropriate - we have permission for these - We want to see a at least three options for these screens to .

We need designs within 3 days

```html
<!DOCTYPE html>
<html lang="en">
<head>
<meta charset="utf-8">
<title>Bright Harbor – Easter Screens</title>
<link href="https://fonts.googleapis.com/css2?family=Cinzel:wght@500;600;700&display=swap" rel="stylesheet">
<style>
  :root {
    --board: #c0c0c0;
    --ink-dark: #222224;
    --ink-amber: #b8731c;
    --bronze: #8a5a22;
    --cream: #f9f0e8;
    --slate: #5a5b5e;
    --mist: #f2f2f2;
    --white: #ffffff;
    --lilac: #d8c8ea;
    --gold: #fcd05a;
  }
  * { margin: 0; padding: 0; box-sizing: border-box; }
  html, body { width: 1200px; height: 1200px; overflow: hidden; }
  body {
    background: var(--board);
    font-family: "Cinzel", serif;
    position: relative;
  }
  .screen {
    position: absolute;
    left: 340px;
    width: 530px;
    height: 298px;
    overflow: hidden;
    box-shadow: 0 6px 14px rgba(0,0,0,0.45);
  }
  .screen--friday { top: 96px; background: var(--white); }
  .screen--sunday { top: 452px; background: var(--cream); }
  .screen--message { top: 812px; background: linear-gradient(160deg, #ececec, var(--mist) 50%, #fafafa); }

  .title { position: absolute; line-height: 1; font-weight: 600; white-space: nowrap; }
  .title .cap { font-size: 1.22em; }
  .subtitle { position: absolute; font-weight: 600; letter-spacing: 0.02em; white-space: nowrap; }
  .date-band { position: absolute; }
  .date-band span {
    position: absolute; color: var(--white); font-weight: 500;
    font-size: 27px; line-height: 28px; white-space: nowrap;
  }
  .artwork { position: absolute; }

  /* Good Friday */
  .screen--friday .title { color: var(--ink-dark); }
  .screen--friday .title--small { left: 25px; top: 26px; font-size: 50px; }
  .screen--friday .title--large {
    left: 27px; top: 88px; font-size: 58px;
    background: radial-gradient(circle at 30% 55%, var(--ink-amber) 0, #6b4518 22%, var(--ink-dark) 45%);
    -webkit-background-clip: text; background-clip: text; color: transparent;
  }
  .screen--friday .subtitle { left: 25px; top: 168px; font-size: 19px; line-height: 26px; color: var(--ink-dark); white-space: normal; width: 330px; }
  .screen--friday .date-band {
    left: 0; top: 234px; width: 415px; height: 28px;
    background: linear-gradient(90deg, var(--ink-dark) 0, var(--ink-dark) 10%, rgba(34,34,36,0.35) 75%, rgba(34,34,36,0) 100%);
  }
  .screen--friday .date-band span { left: 25px; top: 1px; }
  .screen--friday .artwork {
    left: 372px; top: 0; width: 150px; height: 250px;
    background: radial-gradient(ellipse at 50% 55%, #e4e4e4 0, #f4f4f4 40%, rgba(255,255,255,0) 70%);
  }

  /* Easter Sunday */
  .screen--sunday .title { color: var(--bronze); }
  .screen--sunday .title--small { left: 84px; top: 42px; font-size: 46px; }
  .screen--sunday .title--large { left: 222px; top: 94px; font-size: 56px; }
  .screen--sunday .subtitle { left: 0; width: 530px; text-align: center; top: 187px; font-size: 19px; color: var(--bronze); }
  .screen--sunday .date-band {
    left: 78px; top: 227px; width: 374px; height: 28px;
    background: linear-gradient(90deg, rgba(138,90,34,0) 0, var(--bronze) 35%, var(--bronze) 65%, rgba(138,90,34,0) 100%);
  }
  .screen--sunday .date-band span { left: 0; width: 374px; text-align: center; top: 1px; }
  .screen--sunday .artwork {
    left: 140px; top: 0; width: 240px; height: 290px;
    background: radial-gradient(ellipse 45% 50% at 50% 55%, var(--lilac) 0, #ecd8e4 55%, rgba(249,240,232,0) 100%);
  }

  /* Message */
  .screen--message .title { color: var(--slate); right: 30px; text-align: right; }
  .screen--message .title--small { top: 42px; font-size: 46px; }
  .screen--message .title--large { top: 96px; font-size: 56px; }
  .screen--message .subtitle { left: 0; width: 530px; text-align: center; top: 187px; font-size: 19px; color: var(--slate); }
  .screen--message .date-band {
    left: 151px; top: 227px; width: 379px; height: 28px;
    background: linear-gradient(90deg, rgba(90,91,94,0) 0, rgba(90,91,94,0.5) 35%, var(--slate) 65%);
  }
  .screen--message .date-band span { right: 27px; top: 1px; }
  .screen--message .artwork {
    left: 0; top: 0; width: 275px; height: 298px;
    background: radial-gradient(ellipse 70% 65% at 35% 35%, rgba(252,208,90,0.7) 0, rgba(252,208,90,0.35) 55%, rgba(252,208,90,0) 100%);
  }
</style>
</head>
<body>

  <section class="screen screen--friday" aria-label="Good Friday screen">
    <div class="artwork" role="img" aria-label="Soft grey illustration of a robed figure with two hanging crosses"></div>
    <h1 class="title title--small"><span class="cap">S</span>TILL</h1>
    <h1 class="title title--large"><span class="cap">L</span>ANTERNS</h1>
    <p class="subtitle">Letters Written Beside a Quiet Harbor Gate</p>
    <div class="date-band"><span>1 March – 5 April</span></div>
  </section>

  <section class="screen screen--sunday" aria-label="Easter Sunday screen">
    <div class="artwork" role="img" aria-label="Soft lilac glow with a starburst of light and sparkles"></div>
    <h1 class="title title--small"><span class="cap">B</span>RIGHT</h1>
    <h1 class="title title--large"><span class="cap">H</span>ARBOR</h1>
    <p class="subtitle">Letters Written Beside a Quiet Harbor Gate</p>
    <div class="date-band"><span>1 March – 5 April</span></div>
  </section>

  <section class="screen screen--message" aria-label="Message title screen">
    <div class="artwork" role="img" aria-label="Golden brushstroke cross illustration over a soft grey marbled texture"></div>
    <h1 class="title title--small"><span class="cap">B</span>RIGHT</h1>
    <h1 class="title title--large"><span class="cap">H</span>ARBOR</h1>
    <p class="subtitle">Letters Written Beside a Quiet Harbor Gate</p>
    <div class="date-band"><span>1 March – 5 April</span></div>
  </section>

</body>
</html>
```